Locksmith Services Tri Fold Flyer

We are a security company that provide all forms of security, we are looking to have tri fold flyers created for each service we offer starting with Locksmith Services, I am looking to work with someone who can design the layout and advise where the text would go where the pictures would go etc as well as tweaking our current logo, I am hoping to find someone that I can work with across all marketing materials for the business.

Our company is called Harborline Alliance Holdings , and the Locksmith side will be Harborline Keysmiths which is why the logo will need tweaking but with the text " Part of the Harborline Alliance Holdings "

Logo Text

Our Strap Line is " Protecting People, Property & Assets "

```html
<!DOCTYPE html>
<html lang="en">
<head>
<meta charset="utf-8">
<title>Harborline Keysmiths – Locksmith Services Tri-Fold</title>
<link href="https://fonts.googleapis.com/css2?family=Montserrat:wght@400;500;600;700;800&family=Oswald:wght@500;600&family=Cinzel:wght@400&display=swap" rel="stylesheet">
<style>
:root{
  --ink:#1d1b1a;
  --gold:#b8995a;
  --gold-light:#cdb27a;
  --paper:#ffffff;
  --grey:#5a5a5a;
  --text:#3a3a3a;
  --board:#eeeeee;
}
*{box-sizing:border-box;margin:0;padding:0}
html,body{width:1200px;height:2941px;overflow:hidden}
body{background:var(--board);font-family:"Montserrat",sans-serif;color:var(--text);position:relative}
.spread{position:absolute;left:60px;width:1080px;height:833px;background:var(--paper);display:flex;box-shadow:0 10px 30px rgba(0,0,0,.18)}
.spread-outside{top:600px}
.spread-inside{top:1513px}
.panel{width:360px;height:100%;position:relative;overflow:hidden}
.photo{position:absolute;left:0;width:100%}
.band-dark{background:var(--ink);color:#fff}
.gold{color:var(--gold)}
.body-copy{font-size:11.3px;line-height:1.3;color:var(--text)}
.ticks{list-style:none}
.ticks li{display:flex;align-items:center;gap:9px;font-size:10.6px;font-weight:500;color:var(--ink);margin-bottom:7.6px}
.ticks svg{flex:none;width:11px;height:11px}
.strap-serif{font-family:"Cinzel",serif;color:var(--gold);line-height:1;text-align:center}

/* outside – panel 1 */
.o1-head{position:absolute;top:167px;left:0;width:100%;height:64px;padding:9px 0 0 44px}
.o1-head h2{font-size:19px;font-weight:400;letter-spacing:.5px;line-height:1.15}
.o1-head h2 b{font-weight:800;color:var(--gold)}
.o1-copy{position:absolute;top:243px;left:44px;width:272px;font-size:10.4px;line-height:1.22}
.icon-grid{position:absolute;top:418px;left:44px;width:290px;display:grid;grid-template-columns:1fr 1fr;row-gap:14px}
.icon-grid div{display:flex;align-items:center;gap:9px;font-size:12px;font-weight:600;color:var(--ink)}
.icon-grid svg{width:30px;height:30px;flex:none}
.o1-list{position:absolute;top:500px;left:44px}
.o1-foot{position:absolute;bottom:0;left:0;width:100%;height:64px;padding-top:12px}
.o1-foot .strap-serif{font-size:21px}

/* outside – panel 2 */
.contact{position:absolute;top:602px;left:0;width:100%;padding:13px 20px 0 20px}
.contact h3{font-size:19px;font-weight:400;color:var(--ink);letter-spacing:.5px}
.contact h3 b{color:var(--gold);font-weight:700}
.contact .hours{font-size:11.4px;color:var(--text);margin-bottom:10px}
.contact-row{display:flex;align-items:center;gap:16px;margin-bottom:9px;color:var(--ink);font-weight:600}
.contact-row svg{width:18px;height:18px;flex:none}
.contact-row.phone{font-size:17px;font-weight:700}
.contact-row.small{font-size:11.6px}
.dash{border-top:1.5px dashed var(--ink);margin:8px 20px 10px 0}
.allday{display:flex;align-items:center;gap:8px}
.allday svg{width:44px;height:44px}
.allday .big{font-size:26px;font-weight:800;color:var(--ink);line-height:.9}
.allday .tag{display:inline-block;background:var(--ink);color:var(--gold);font-size:12.5px;font-weight:800;padding:3px 28px 3px 8px;clip-path:polygon(0 0,100% 0,88% 100%,0 100%)}

/* outside – panel 3 */
.brand{position:absolute;top:0;left:0;width:100%;height:312px;display:flex;flex-direction:column;align-items:center;justify-content:center;gap:12px}
.brand-mark{display:flex;align-items:center;gap:10px;font-family:"Montserrat",sans-serif;font-weight:700;font-size:17px;color:var(--gold);letter-spacing:.5px}
.brand-mark i{width:14px;height:14px;border-radius:50%;background:var(--gold);display:block}
.brand .strap-serif{font-size:22px;margin-top:26px}
.brand .part{font-size:10px;color:var(--gold);font-weight:500;letter-spacing:.5px}
.title-band{position:absolute;top:602px;left:0;width:100%;height:167px;background:linear-gradient(90deg,#3b3b3b,#6a6a6a 50%,#3b3b3b);text-align:center;padding-top:18px;color:#fff}
.title-band h1{font-family:"Oswald",sans-serif;font-weight:500;font-size:38px;line-height:1.05;letter-spacing:.3px}
.title-band p{font-size:13px;letter-spacing:.5px;margin-top:10px;line-height:1.25;color:#e6e6e6}
.url-band{position:absolute;bottom:0;left:0;width:100%;height:64px;display:flex;align-items:center;justify-content:center;font-family:"Oswald",sans-serif;font-size:20px;color:var(--gold);letter-spacing:.2px}

/* inside */
.in-photo{position:absolute;top:0;height:210px}
.in-rule{position:absolute;top:210px;left:0;width:100%;height:6px;background:var(--ink)}
.label{position:absolute;top:222px;left:0;height:24px;padding:1px 38px 0 40px;background:var(--ink);color:var(--gold);font-weight:800;font-size:17px;letter-spacing:.5px;clip-path:polygon(0 0,100% 0,86% 100%,0 100%)}
.inner{position:absolute;top:256px;left:40px;width:300px}
.inner h3{font-size:15px;font-weight:700;color:var(--ink);line-height:1.05;letter-spacing:.3px}
.inner h3 span{color:var(--gold);display:block}
.inner .body-copy{margin:14px 0 0;font-size:10.8px}
.inner h4{font-size:15px;font-weight:700;color:var(--ink);line-height:1.05;margin-top:20px}
.inner h4 span{color:var(--gold);display:block}
.inner .ticks{margin-top:16px}
.inner .ticks li{font-size:10.2px;margin-bottom:9.3px}
.dashbox{border-top:1.5px dashed var(--ink);margin-top:6px;padding-top:6px}
.dashbox strong{font-size:14px;font-weight:700;color:var(--ink);display:block;letter-spacing:.3px}
.dashbox span{font-size:11px;color:var(--ink)}
.dashbox-end{border-bottom:1.5px dashed var(--ink);padding-bottom:8px}
.service-row{display:flex;align-items:center;gap:12px;font-size:11px;font-weight:700;color:var(--ink);margin-bottom:13px;line-height:1.2}
.service-row svg{width:30px;height:30px;flex:none}
</style>
</head>
<body>

<svg width="0" height="0" style="position:absolute" aria-hidden="true">
  <defs>
    <symbol id="tick" viewBox="0 0 12 12"><circle cx="6" cy="6" r="6" fill="#b8995a"/><path d="M3.3 6.2l1.9 1.9 3.6-3.8" fill="none" stroke="#fff" stroke-width="1.5"/></symbol>
    <symbol id="badge-bell" viewBox="0 0 32 32"><circle cx="16" cy="16" r="15" fill="#b8995a" stroke="#1d1b1a" stroke-width="2"/><path d="M10 21h12l-2-3v-4a4 4 0 0 0-8 0v4z" fill="#1d1b1a"/><circle cx="16" cy="23" r="1.6" fill="#1d1b1a"/></symbol>
    <symbol id="badge-house" viewBox="0 0 32 32"><circle cx="16" cy="16" r="15" fill="#b8995a" stroke="#1d1b1a" stroke-width="2"/><path d="M9 16l7-6 7 6v7H9z" fill="#1d1b1a"/><rect x="14.5" y="18" width="3" height="5" fill="#b8995a"/></symbol>
    <symbol id="badge-car" viewBox="0 0 32 32"><circle cx="16" cy="16" r="15" fill="#b8995a" stroke="#1d1b1a" stroke-width="2"/><path d="M8 19v-3l2-4h12l2 4v3z" fill="#1d1b1a"/><circle cx="11.5" cy="20" r="1.8" fill="#1d1b1a"/><circle cx="20.5" cy="20" r="1.8" fill="#1d1b1a"/></symbol>
    <symbol id="badge-building" viewBox="0 0 32 32"><circle cx="16" cy="16" r="15" fill="#b8995a" stroke="#1d1b1a" stroke-width="2"/><rect x="10" y="9" width="12" height="14" fill="#1d1b1a"/><path d="M12.5 12h2M17.5 12h2M12.5 15h2M17.5 15h2M12.5 18h2M17.5 18h2" stroke="#b8995a" stroke-width="1.4"/></symbol>
    <symbol id="badge-lock" viewBox="0 0 32 32"><circle cx="16" cy="16" r="15" fill="#b8995a" stroke="#1d1b1a" stroke-width="2"/><rect x="10.5" y="15" width="11" height="8" rx="1" fill="#1d1b1a"/><path d="M12.5 15v-3a3.5 3.5 0 0 1 7 0v3" fill="none" stroke="#1d1b1a" stroke-width="2"/></symbol>
    <symbol id="badge-key" viewBox="0 0 32 32"><circle cx="16" cy="16" r="15" fill="#b8995a" stroke="#1d1b1a" stroke-width="2"/><circle cx="12" cy="16" r="3.5" fill="none" stroke="#1d1b1a" stroke-width="2.2"/><path d="M15.5 16h8M21 16v3M23.5 16v2.5" stroke="#1d1b1a" stroke-width="2.2"/></symbol>
  </defs>
</svg>

<!-- Outside spread -->
<section class="spread spread-outside">
  <div class="panel">
    <div class="photo" style="top:0;height:167px;background:linear-gradient(120deg,#4a4fa0 0 28%,#d8dde4 28%,#b9c0c9)" role="img" aria-label="Hand holding a smartphone next to a smart electronic door lock"></div>
    <div class="o1-head band-dark"><h2>EMERGENCY <b>LOCKSMITH</b><br><b>SERVICES</b></h2></div>
    <p class="o1-copy body-copy">It is a long established fact that a reader will be distracted by the readable content of a page when looking at its layout. The point of using Lorem Ipsum is that it has a more-or-less normal distribution of letters, as opposed to using 'Content here, content here', making it look like readable English. Many desktop publishing packages and web page editors now use Lorem Ipsum as their default model text, and a search for 'lorem ipsum' will uncover many web sites still in their infancy. Various versions have evolved over the years, sometimes by accident, sometimes on purpose</p>
    <div class="icon-grid">
      <div><svg><use href="#badge-bell"/></svg>EMERGENCY</div>
      <div><svg><use href="#badge-building"/></svg>RESIDENTIAL</div>
      <div><svg><use href="#badge-car"/></svg>AUTOMOTIVE</div>
      <div><svg><use href="#badge-house"/></svg>COMMERCIAL</div>
    </div>
    <ul class="o1-list ticks">
      <li><svg><use href="#tick"/></svg>24hr Emergency Lockouts / Openings</li>
      <li><svg><use href="#tick"/></svg>Automobile / Car Entry</li>
      <li><svg><use href="#tick"/></svg>Open Filing Cabinets</li>
      <li><svg><use href="#tick"/></svg>Open Mailboxes locks</li>
      <li><svg><use href="#tick"/></svg>Burglary / Break in Repairs</li>
      <li><svg><use href="#tick"/></svg>Open locked car door / Trunk / fuel door</li>
      <li><svg><use href="#tick"/></svg>Open locked / Stuck garage door</li>
      <li><svg><use href="#tick"/></svg>Open automatic driveway gates</li>
      <li><svg><use href="#tick"/></svg>Open / Repair any type of safe</li>
      <li><svg><use href="#tick"/></svg>Open High security locks</li>
    </ul>
    <div class="o1-foot band-dark"><p class="strap-serif">PROTECTING PEOPLE,<br>PROPERTY &amp; ASSETS</p></div>
  </div>

  <div class="panel">
    <div class="photo" style="top:0;height:172px;background:linear-gradient(90deg,#bdbdbd,#efefef 50%,#a9a9a9)" role="img" aria-label="Black and white close-up of a door handle and latch"></div>
    <div class="photo" style="top:172px;height:430px;background:radial-gradient(circle at 50% 45%,#2fb7c9 0,#13505e 45%,#1b2227 85%)" role="img" aria-label="Digital security network graphic with a combination padlock on a cable"></div>
    <div class="contact">
      <h3>CONTACT <b>US</b></h3>
      <p class="hours">Between 7 AM and 12 AM EST, 7 days a week</p>
      <div class="contact-row phone"><svg viewBox="0 0 20 20"><path d="M5 2l3 4-2 2a11 11 0 0 0 6 6l2-2 4 3-2 3C9 18 2 11 2 4z" fill="none" stroke="#b8995a" stroke-width="1.8"/></svg>1-844-555-0199</div>
      <div class="contact-row small"><svg viewBox="0 0 20 20"><rect x="2" y="4" width="16" height="12" fill="none" stroke="#b8995a" stroke-width="1.8"/><path d="M2 4l8 7 8-7" fill="none" stroke="#b8995a" stroke-width="1.8"/></svg>info@harborlinealliance.com</div>
      <div class="contact-row small"><svg viewBox="0 0 20 20"><circle cx="10" cy="10" r="8" fill="none" stroke="#b8995a" stroke-width="1.8"/><path d="M2 10h16M10 2c-4 4-4 12 0 16M10 2c4 4 4 12 0 16" fill="none" stroke="#b8995a" stroke-width="1.4"/></svg>www.harborlinealliance.com</div>
      <div class="dash"></div>
      <div class="allday">
        <svg viewBox="0 0 44 44"><circle cx="22" cy="22" r="19" fill="none" stroke="#b8995a" stroke-width="2.5"/><path d="M22 10v12l8 5" fill="none" stroke="#b8995a" stroke-width="2.5"/></svg>
        <div><div class="big">24x7</div><span class="tag">EMERGENCY SERVICES</span></div>
      </div>
    </div>
  </div>

  <div class="panel">
    <div class="brand">
      <div class="brand-mark"><i></i>HARBORLINE KEYSMITHS</div>
      <div class="part">Part of the Harborline Alliance Holdings</div>
      <p class="strap-serif">PROTECTING PEOPLE,<br>PROPERTY &amp; ASSETS</p>
    </div>
    <div class="photo" style="top:312px;height:290px;background:linear-gradient(90deg,#3a2412,#b0662a 35%,#e2b78a 70%,#8a5a35)" role="img" aria-label="Locksmith using a screwdriver on a door lock"></div>
    <div class="title-band">
      <h1>PROTECTING PEOPLE<br>PROPERTY &amp; ASSETS</h1>
      <p>WE ARE A SECURITY COMPANY THAT<br>PROVIDE ALL FORMS OF SECURITY</p>
    </div>
    <div class="url-band band-dark">HARBORLINEALLIANCE.COM</div>
  </div>
</section>

<!-- Inside spread -->
<section class="spread spread-inside">
  <div class="panel">
    <div class="in-photo photo" style="background:linear-gradient(90deg,#e4c04a,#3c3f54 45%,#c9c9c9 80%,#5a4a3a)" role="img" aria-label="Locksmith with a power drill fitting a lock"></div>
    <div class="in-rule"></div>
    <div class="label">EMERGENCY</div>
    <div class="inner">
      <h3>QUICK AND RELIABLE<span>EMERGENCY LOCKSMITH</span><span>SERVICE</span></h3>
      <p class="body-copy">It is a long established fact that a reader will be distracted by the readable content of a page when looking at its layout. The point of using Lorem Ipsum is that it has a more-or-less normal distribution of letters, as opposed to using 'Content here, content here', making it look like readable English. Many desktop publishing packages and web page editors now use Lorem Ipsum as their default model text, and a search for 'lorem ipsum' will uncover many web sites still in their infancy. Various versions have evolved over the years, sometimes by accident, sometimes on purpose</p>
      <h4>WE OFFER THE FOLLOWING<span>EMERGENCY LOCKSMITH</span><span>SERVICES:</span></h4>
      <ul class="ticks">
        <li><svg><use href="#tick"/></svg>Emergency Lockout Services for Homes,<br>Commercial Buildings, and Vehicles</li>
        <li><svg><use href="#tick"/></svg>Lock Changes and Repair</li>
        <li><svg><use href="#tick"/></svg>Re-Keying</li>
        <li><svg><use href="#tick"/></svg>Keyless Entry Systems</li>
        <li><svg><use href="#tick"/></svg>Master Key Systems</li>
        <li><svg><use href="#tick"/></svg>Panic Bar Repair and Installation</li>
        <li><svg><use href="#tick"/></svg>Access Control Systems</li>
      </ul>
      <div class="dashbox dashbox-end"><strong>WE ARE AVAILABLE 24/7 FOR ANY</strong><span>Emergency Locksmith requirement!</span></div>
    </div>
  </div>

  <div class="panel">
    <div class="in-photo photo" style="background:linear-gradient(90deg,#d9d9d9,#3558a8 40%,#e9e9e9 75%,#cfcfcf)" role="img" aria-label="Locksmith opening a white car door lock"></div>
    <div class="in-rule"></div>
    <div class="label">AUTOMOTIVE</div>
    <div class="inner">
      <h3>QUICKLY GETTING YOU ON<br>THE ROAD AGAIN<span>MOBILE EXPERT AUTO KEY</span><span>DUPLICATION &amp; REPLACEMENT</span></h3>
      <p class="body-copy">It is a long established fact that a reader will be distracted by the readable content of a page when looking at its layout.</p>
      <div class="dashbox" style="margin-top:14px"></div>
      <h4 style="margin-top:12px">CAR KEY REPLACEMENT AND<br>DUPLICATION SERVICES<span>HARBORLINE KEYSMITHS OFFERS</span><span>THE FOLLOWING AUTOMOTIVE</span><span>KEY SERVICES:</span></h4>
      <ul class="ticks">
        <li><svg><use href="#tick"/></svg>Transponder (remote and key FOB) replacement</li>
        <li><svg><use href="#tick"/></svg>Transponder chip repair, duplication, &amp; replacement</li>
        <li><svg><use href="#tick"/></svg>Smart and Flip Blade key repair or replacement</li>
        <li><svg><use href="#tick"/></svg>VAT key copying</li>
        <li><svg><use href="#tick"/></svg>VIN key copying</li>
        <li><svg><use href="#tick"/></svg>PROX Car Key duplication and replacement</li>
        <li><svg><use href="#tick"/></svg>Immobilizer key reprogramming</li>
        <li><svg><use href="#tick"/></svg>Car remote programming</li>
        <li><svg><use href="#tick"/></svg>Ignition switch repair and unlocking</li>
        <li><svg><use href="#tick"/></svg>Broken key removal</li>
        <li><svg><use href="#tick"/></svg>Car trunk opening</li>
        <li><svg><use href="#tick"/></svg>High Security Car Key Cutting</li>
      </ul>
    </div>
  </div>

  <div class="panel">
    <div class="in-photo photo" style="background:linear-gradient(90deg,#cfd6dc,#3a3c44 40%,#c28a55 75%,#e7c9a3)" role="img" aria-label="Locksmith installing a mortise lock in a door edge"></div>
    <div class="in-rule"></div>
    <div class="label">RESIDENTIAL</div>
    <div class="inner">
      <h3>LOCKSMITH SERVICES TO<span>PROTECT YOUR HOME &amp; FAMILY</span></h3>
      <p class="body-copy" style="margin-bottom:14px">It is a long established fact that a reader will be distracted by the readable content of a page when looking at its layout.</p>
      <div class="service-row"><svg><use href="#badge-key"/></svg>HOME LOCKOUT SERVICE</div>
      <div class="service-row"><svg><use href="#badge-lock"/></svg>LOCK INSTALLATION,<br>REPLACEMENT, AND REPAIR</div>
      <div class="service-row"><svg><use href="#badge-house"/></svg>LOCK REKEYING</div>
      <h4>HARBORLINE KEYSMITHS'<span>COMPREHENSIVE RANGE OF</span><span>SERVICES</span></h4>
      <ul class="ticks">
        <li><svg><use href="#tick"/></svg>Deadbolt installation</li>
        <li><svg><use href="#tick"/></svg>Rekeying existing locks and deadbolts</li>
        <li><svg><use href="#tick"/></svg>Gate, garage, and fencing locks</li>
        <li><svg><use href="#tick"/></svg>Cabinet, drawer, bar, and showcase locks</li>
        <li><svg><use href="#tick"/></svg>Pushbutton locks</li>
        <li><svg><use href="#tick"/></svg>Mortise locks</li>
        <li><svg><use href="#tick"/></svg>Patio door bars</li>
        <li><svg><use href="#tick"/></svg>Jimmy proof locks</li>
        <li><svg><use href="#tick"/></svg>Key cabinets and storage boxes</li>
        <li><svg><use href="#tick"/></svg>Digital deadbolts</li>
        <li><svg><use href="#tick"/></svg>Lever locks</li>
      </ul>
    </div>
  </div>
</section>

</body>
</html>
```